Flyer-Design für Physiotherapie-Praxis
Zielgruppe
Wir sind eine Praxis für Physiotherapie und möchten durch diesen Flyer neue Patienten werben. Der Flyer soll in Arztpraxen ausliegen und dort den Patienten direkt ansprechen und auf uns aufmerksam machen. Es ist auch eine Verknüpfung der Therapie mit einem Training in einem Gesundheitsstudio möglich, da im gleichen Haus das Physio Kraftwerk Eichenstetten beheimatet ist.
Aufgabenstellung
Der Fokus auf unsere Prinzipien (Ganzheitliche Therapie, hohes Maß an Therapiemöglichkeiten, Variation in den therapeutischen Ansätzen durch unterschiedlich fortgebildete Therapeuten, die nach den gleichen Idealen arbeiten)

```html
<!DOCTYPE html>
<html lang="de">
<head>
<meta charset="utf-8">
<title>Flyer – Zentrum für Therapie &amp; Training</title>
<link rel="stylesheet" href="https://fonts.googleapis.com/css2?family=Montserrat:wght@300;400;600;700&family=Michroma&display=swap">
<style>
  :root {
    --bg: #d8d9dc;
    --paper: #ffffff;
    --paper-soft: #f1f1f2;
    --blue-light: #4fb3e2;
    --blue-mid: #2a93d4;
    --blue-deep: #1b5fae;
    --navy: #1d3f86;
    --grey-text: #8a8c90;
    --grey-head: #6c6e72;
    --white-text: #f4fbff;
  }
  * { box-sizing: border-box; margin: 0; padding: 0; }
  html, body { width: 1200px; height: 900px; overflow: hidden; }
  body {
    background: var(--bg);
    font-family: "Montserrat", sans-serif;
    position: relative;
  }
  .flyer {
    position: absolute;
    top: 120px;
    width: 300px;
    height: 660px;
    overflow: hidden;
    box-shadow: 0 10px 30px rgba(0,0,0,.12);
  }
  /* Cover panel */
  .cover { left: 110px; background: var(--paper); }
  .cover-brand {
    position: absolute; top: 60px; left: 0; right: 0;
    text-align: center; padding: 0 24px;
  }
  .brand-mark {
    display: inline-flex; align-items: center; gap: 8px;
    font-weight: 600; font-size: 15px; color: var(--blue-mid);
    margin-bottom: 40px;
  }
  .brand-mark .dot { width: 12px; height: 12px; border-radius: 50%; background: var(--blue-mid); }
  .cover-kicker { font-size: 10.5px; font-weight: 300; color: var(--blue-mid); letter-spacing: .3px; }
  .cover-names { font-size: 18px; font-weight: 600; color: var(--navy); margin: 4px 0; }
  .cover-owner { font-size: 10px; font-weight: 300; color: var(--blue-mid); }
  .cover-wave { position: absolute; top: 240px; left: 0; width: 300px; height: 420px; }
  .cover-text {
    position: absolute; top: 290px; left: 26px; right: 22px;
    color: var(--white-text);
  }
  .cover-title { font-size: 15px; font-weight: 300; line-height: 1.25; margin-bottom: 16px; }
  .cover-title strong { font-weight: 700; }
  .cover-text p { font-size: 9.2px; font-weight: 300; line-height: 1.55; margin-bottom: 12px; }
  .cover-text p b { font-weight: 700; }

  /* Inner panel */
  .inner {
    left: 450px;
    background: linear-gradient(160deg, var(--blue-light) 0%, var(--blue-mid) 45%, var(--blue-deep) 100%);
    color: var(--white-text);
  }
  .inner-title {
    font-family: "Michroma", sans-serif;
    font-size: 19px; line-height: 1.35; letter-spacing: 1px;
    padding: 52px 26px 0;
  }
  .inner-lead { font-size: 11px; font-weight: 400; line-height: 1.55; padding: 26px 26px 0; }
  .inner-lead b { font-weight: 700; }
  .inner-body { font-size: 11px; font-weight: 300; line-height: 1.55; padding: 18px 26px 0; }
  .inner-photo {
    position: absolute; left: 0; right: 0; bottom: 0; height: 210px;
    background: linear-gradient(180deg, #c9d3d6 0%, #4a7a48 40%, #1d4f7e 75%, #0e2f5c 100%);
    border-radius: 150px 150px 0 0 / 60px 60px 0 0;
  }

  /* Contact panel */
  .contact { left: 790px; background: var(--paper-soft); padding: 70px 30px 0; }
  .contact-title {
    font-family: "Michroma", sans-serif;
    font-size: 21px; color: var(--blue-mid); letter-spacing: 1.5px;
    margin-bottom: 22px;
  }
  .contact-head {
    font-family: "Michroma", sans-serif;
    font-size: 11.5px; color: var(--grey-head); letter-spacing: 1px;
    margin: 18px 0 10px;
  }
  .contact p { font-size: 11px; font-weight: 300; color: var(--grey-text); line-height: 1.55; margin-bottom: 10px; }
  .contact-brand {
    position: absolute; bottom: 70px; left: 0; right: 0; text-align: center;
  }
  .contact-brand .brand-mark { color: var(--grey-head); margin: 0; }
  .contact-brand .dot { background: var(--grey-head); }
</style>
</head>
<body>

<section class="flyer cover">
  <div class="cover-brand">
    <div class="brand-mark"><span class="dot"></span>Lukas Brenner &amp; Sabine Kolb</div>
    <div class="cover-kicker">ZENTRUM FÜR THERAPIE &amp; TRAINING</div>
    <div class="cover-names">Lukas Brenner &amp; Sabine Kolb</div>
    <div class="cover-owner">Inhaber: Sabine Kolb</div>
  </div>
  <svg class="cover-wave" viewBox="0 0 300 420" preserveAspectRatio="none" aria-hidden="true">
    <path d="M0 40 Q150 -10 300 10 L300 420 L0 420 Z" fill="#4fb3e2"/>
  </svg>
  <div class="cover-text">
    <h2 class="cover-title">WIR SIND THERAPEUTEN<br>AUS <strong>ÜBERZEUGUNG!</strong></h2>
    <p>Unsere Praxis gibt es <b>seit 1969</b>. In dieser Zeit konnten wir viel Erfahrung sammeln.</p>
    <p><b>Wir</b> sind ein Team aus älteren und jüngeren Therapeuten, aus Masseuren, med. Bademeistern und Physiotherapeuten. Diese bunte Mischung beinhaltet viel <b>Erfahrung</b> und viel <b>Wissen</b>. Beides wird in regelmäßigen internen Fortbildungen ausgetauscht. So ergänzen wir uns stets gegenseitig.</p>
    <p><b>Wir</b> arbeiten als Team <b>Hand in Hand</b> und schätzen das Fachwissen jedes einzelnen Kollegen.</p>
    <p><b>Wir</b> sind <b>motiviert</b> und mit <b>Freude</b> bei der Arbeit, denn wir wissen, was unsere Patienten mit Hilfe der Physiotherapie erreichen können.</p>
  </div>
</section>

<section class="flyer inner">
  <h2 class="inner-title">VIELFALT AN THERAPIE-MÖGLICH-KEITEN</h2>
  <p class="inner-lead">Mit modernen <b>Therapiegeräten</b> zur Unterstützung, z.B. eine Kletterwand, eine Vibrano®-Rüttelplatte, ein <b>Bewegungsbad</b>!</p>
  <p class="inner-body">Dabei ergänzen sich unsere Therapeuten mit unserem Fachwissen. Langjährig haben wir uns auf orthopädischer, chirurgischer Nachsorge spezialisiert.</p>
  <div class="inner-photo" role="img" aria-label="Foto des Bewegungsbads mit Pflanzen und Glasdach"></div>
</section>

<section class="flyer contact">
  <h2 class="contact-title">KONTAKT</h2>
  <h3 class="contact-head">ANFAHRT</h3>
  <p>Zentrum für Therapie und Training<br>Lukas Brenner &amp; Sabine Kolb</p>
  <p>Lindenweg 27<br>91234 Eichenstetten-Süd</p>
  <h3 class="contact-head">INHABER</h3>
  <p>Frau Sabine Kolb</p>
  <div class="contact-brand">
    <div class="brand-mark"><span class="dot"></span>Lukas Brenner &amp; Sabine Kolb</div>
  </div>
</section>

</body>
</html>
```